Our company is Harlow Rivet & Pin Inc. We serve the OEM Market and have customers across the globe. Custom fastening parts made to print as well as standard fasteners, abrasives, adhesives and vendor managed inventory services. We pride ourselves on reliability, partnership and overall lowest cost of business, with an emphasis on quality and attention to detail. Harlow Rivet does not simply provide products, we provide solutions to save our customers time and money in their supply chain as well as on their assembly lines. Our Customers are in Telecom, Metering, Nuclear, Packaging Equipment, Networking Component, Boat Trailer, Portable Military and Camp Shelters, Knife and Locomotive Heater Industries (varied, but all OEM's). 95% of our customers use Lean and Six Sigma in their operations, and we customize our Vendor Managed Inventory Systems to suit each customer's individual supply chain goals. We have a mechanical engineer on staff who oversees our quality and conformance lab to ensure that customer parts are made to their exacting specifications. We incorporate continuous improvement in every process and task in our business. Texas Orange and Black are the main colors we utilize in our marketing. The final design should communicate reliability, innovation, technical superiority, as well as partnership.

Target Market(s)

Original Equipment Manufacturers - Electronic and Industrial

Industry/Entity Type

Business

Requirements
Must have
• Some animation...eye catching, but not distracting. A contact/request for quote page that connects to a company email address. A balance of graphics, photos and written content. Must be able to edit in Expression Web.

You may use the written content and any photos from our current website www.harlowrivet-sample.com
Should not have
• No cartoons, please.

```html
<!DOCTYPE html>
<html lang="en">
<head>
<meta charset="utf-8">
<title>Harlow Rivet &amp; Pin Inc.</title>
<link rel="stylesheet" href="https://fonts.googleapis.com/css2?family=PT+Sans:wght@400;700&family=Open+Sans:wght@400;600;700&display=swap">
<style>
:root{
  --orange:#e8621c;
  --orange-dark:#c94d10;
  --ink:#1a1a1a;
  --text:#333;
  --muted:#888;
  --rule:#ddd;
  --panel:#ebebeb;
  --footer:#222;
  --footer-deep:#111;
  --footer-text:#8a8a8a;
}
*{box-sizing:border-box;margin:0;padding:0}
html,body{width:973px;height:1200px;overflow:hidden}
body{position:relative;background:#fff;font-family:"Open Sans",Arial,sans-serif;color:var(--text);font-size:11px}
a{color:inherit;text-decoration:none}
.page-top{position:absolute;left:0;top:0;width:973px;height:400px;background:linear-gradient(#d6d6d6,#eeeeee 55%,#fff)}
.utility{position:absolute;right:150px;top:5px;font-size:10px;color:#333}
.utility span{margin:0 5px}
.tollfree{position:absolute;right:149px;top:23px;font:700 11px "Open Sans",sans-serif;color:var(--ink);display:flex;align-items:center;gap:5px}
.nav-stub{position:absolute;left:172px;top:44px;width:29px;height:32px;background:linear-gradient(#333,#000)}
.brand{position:absolute;left:204px;top:35px;width:166px;height:46px;background:#111;border:2px solid #fff;outline:1px solid #000;display:flex;align-items:center;gap:10px;padding-left:3px}
.brand-mark{width:38px;height:38px;background:var(--orange)}
.brand-name{font:700 26px "PT Sans",sans-serif;color:#fff;letter-spacing:.5px}
.main-nav{position:absolute;left:374px;top:43px;width:450px;height:33px;background:linear-gradient(#3a3a3a,#050505);display:flex}
.main-nav a{color:#fff;font:400 11.5px "PT Sans",sans-serif;line-height:33px;text-align:center;border-right:1px solid #444}
.main-nav a:last-child{border:0}
.hero-photo{position:absolute;left:160px;top:118px;width:352px;height:224px;background:radial-gradient(ellipse at 50% 55%,#c9d4dc,#9fb0bd 45%,rgba(235,235,235,0) 72%)}
.hero-copy{position:absolute;right:170px;top:162px;text-align:right}
.hero-copy h1{font:700 29px/34px "PT Sans",sans-serif;color:var(--ink)}
.hero-copy p{font:400 19px/22px "PT Sans",sans-serif;color:#333;margin-top:6px}
.btn{display:inline-block;background:linear-gradient(#f07a2e,var(--orange-dark));color:#fff;border:1px solid #b8450d;border-radius:2px;font:700 12px "PT Sans",sans-serif}
.hero-copy .btn{margin-top:23px;width:84px;height:22px;line-height:20px;text-align:center}
.hero-rule{position:absolute;left:260px;top:383px;width:450px;height:4px;background:radial-gradient(ellipse at center,rgba(0,0,0,.12),rgba(0,0,0,0) 70%)}
.section-title{font:700 16px "PT Sans",sans-serif;color:var(--orange)}
.welcome{position:absolute;left:172px;top:420px;width:430px;line-height:14.7px}
.welcome .section-title{margin-bottom:12px}
.welcome-photo{float:left;width:135px;height:97px;margin:0 10px 4px 0;background:linear-gradient(90deg,#6a4e36,#b7a48a 35%,#e4dccb 50%,#a28c72 65%,#5d4632)}
.welcome p+p{margin-top:14px}
.more{color:var(--orange)}
.quote{position:absolute;left:615px;top:415px;width:209px;height:217px;background:var(--panel);padding:10px 16px}
.quote .section-title{font-size:17px;margin-bottom:9px}
.field{display:block;width:177px;height:22px;background:#fff;border:1px solid #ccc;border-radius:3px;font-size:9.5px;color:#999;padding:4px 6px;margin-bottom:8px}
.field.msg{height:36px}
.quote .btn{display:block;margin:5px auto 0;width:134px;height:23px;line-height:21px;text-align:center;font-size:12.5px}
.mid-rule{position:absolute;left:155px;top:653px;width:663px;border-top:1px solid #e6e6e6}
.col{position:absolute;top:681px;width:210px}
.col h2{font:700 12.5px "PT Sans",sans-serif;color:var(--orange);margin-bottom:12px}
.news-item{border-bottom:1px solid var(--rule);padding-bottom:8px;margin-bottom:8px;width:208px;font-size:9.5px;line-height:12.5px}
.news-item time{color:var(--muted);font-size:9px}
.news-item b{display:block;color:var(--ink)}
.features li{list-style:none;font:600 9.5px/12px "Open Sans",sans-serif;color:var(--ink);margin-bottom:6px;padding-left:12px;position:relative}
.features li.plain{padding-left:0}
.features li:not(.plain)::before,.lean li::before{content:"";position:absolute;left:3px;top:4px;width:4px;height:4px;background:var(--orange);transform:rotate(45deg)}
.lean h3{font:600 9.5px/12.5px "Open Sans",sans-serif;color:var(--ink);margin-bottom:1px}
.lean ul{margin-bottom:12px}
.lean li{list-style:none;position:relative;padding-left:12px;font-size:9.5px;line-height:14px;color:#555}
.col .more{font-size:9.5px}
.partners{position:absolute;left:140px;top:943px;width:710px;height:72px;background:#fff;box-shadow:0 0 10px rgba(0,0,0,.08)}
.partners h2{position:absolute;left:36px;top:25px;font:700 12.5px "PT Sans",sans-serif;color:var(--orange)}
.partners svg{position:absolute;left:110px;top:17px}
.badge{position:absolute;top:12px;height:46px;border:1px solid #ccc;display:flex;align-items:center;justify-content:center}
.badge span{display:block;background:#c9c9c9;border-radius:14px}
.site-footer{position:absolute;left:0;top:1041px;width:973px;height:113px;background:var(--footer);color:var(--footer-text);font-size:9.5px}
.site-footer h2{font:400 11px "Open Sans",sans-serif;color:#ddd;margin-bottom:8px}
.f-menu{position:absolute;left:173px;top:10px}
.f-menu ul{list-style:none;position:absolute;top:24px;width:80px}
.f-menu li{line-height:17px;padding-left:15px;position:relative}
.f-menu li::before{content:"";position:absolute;left:4px;top:7px;width:3px;height:3px;border-radius:50%;background:#666}
.f-sep{position:absolute;top:12px;width:1px;height:92px;background:#333}
.f-contact{position:absolute;left:349px;top:13px;width:300px;line-height:14px}
.f-contact address{font-style:normal;position:absolute;top:20px}
.f-contact dl{position:absolute;left:132px;top:20px;display:grid;grid-template-columns:66px auto}
.f-contact dd u{text-decoration:underline}
.f-social{position:absolute;left:673px;top:13px}
.f-social li{list-style:none;display:flex;align-items:center;gap:6px;height:20px}
.f-social i{width:14px;height:14px;border-radius:50%;background:#555;display:block;margin-left:9px}
.legal{position:absolute;left:0;top:1154px;width:973px;height:46px;background:var(--footer-deep);color:#777;font-size:8.5px;text-align:center;padding-top:7px;line-height:13px}
</style>
</head>
<body>
<div class="page-top"></div>

<header>
  <div class="utility"><a href="#">Employment</a><span>|</span><a href="#">Site Map</a></div>
  <div class="tollfree">
    <svg width="11" height="11" viewBox="0 0 11 11"><rect width="11" height="11" rx="2" fill="#e8621c"/><path d="M3 2.5c.6-.4 1.1-.2 1.4.4l.4.9c.2.4 0 .7-.3.9l-.3.2c.3.8.9 1.4 1.7 1.8l.2-.3c.2-.3.6-.5 1-.3l.9.4c.5.3.7.8.3 1.4-.6.7-1.5.8-2.5.3C4.3 7.4 3.4 6.4 2.8 5 2.3 3.9 2.4 3 3 2.5z" fill="#fff"/></svg>
    TOLL FREE USA: +1 555 014 2290
  </div>
  <div class="nav-stub"></div>
  <a class="brand" href="#"><span class="brand-mark"></span><span class="brand-name">harlow</span></a>
  <nav class="main-nav">
    <a href="#" style="width:74px">HOME</a>
    <a href="#" style="width:87px">ABOUT US</a>
    <a href="#" style="width:95px">PRODUCTS</a>
    <a href="#" style="width:94px">FEATURES</a>
    <a href="#" style="width:100px">CONTACT US</a>
  </nav>
</header>

<section class="hero">
  <div class="hero-photo" role="img" aria-label="Photograph of steel hex bolts and nuts"></div>
  <div class="hero-copy">
    <h1>HIGH QUALITY,<br>STRONG RELATIONSHIP</h1>
    <p>Lorem ipsum dolor sit amet,<br>consectetuer adipiscing elit.</p>
    <a class="btn" href="#">Read More »</a>
  </div>
  <div class="hero-rule"></div>
</section>

<section class="welcome">
  <h2 class="section-title">Welcome to Harlow Rivet Online</h2>
  <div class="welcome-photo" role="img" aria-label="Photograph of warehouse shelving stocked with parts bins"></div>
  <p>Since 1972, Harlow Rivet's mission has been to form strong partnerships with top Upper Valley companies who share the philosophy of exceptional quality and high integrity.<br>We continue to be successful by focusing on our customers' needs by providing many value-added services as well as treating them <b style="color:var(--ink)">fairly, ethically and competitively</b> with every transaction. Our VMI (keepfill) programs are electronically set to your maximum desired quantities...we will not overstock your bins Etiam rhoncus.</p>
  <p>Maecenas tempus, tellus eget condimentum rhoncus, sem quam semper libero, sit amet adipiscing sem neque sed ipsum. Nam quam nunc, blandit vel, luctus pulvinar, hendrerit id, lorem.... <a class="more" href="#">more »</a></p>
</section>

<form class="quote">
  <h2 class="section-title">Request a Free Quote</h2>
  <span class="field">Full Name</span>
  <span class="field">Your Email</span>
  <span class="field">Phone Number</span>
  <span class="field msg">Message</span>
  <span class="btn">Submit Your Request</span>
</form>

<div class="mid-rule"></div>

<section class="col" style="left:172px">
  <h2>Company News</h2>
  <article class="news-item"><time>25th March 2013</time><b>Lorem ipsum dolor sit amet, consectetuer</b>Etiam rhoncus. Maecenas tempus, tellus eget condimentum rhoncus, sem ... <a class="more" href="#">more »</a></article>
  <article class="news-item"><time>25th March 2013</time><b>Lorem ipsum dolor sit amet, consectetuer</b>Etiam rhoncus. Maecenas tempus, tellus eget condimentum rhoncus, sem ... <a class="more" href="#">more »</a></article>
  <article class="news-item" style="border:0"><time>25th March 2013</time><b>Lorem ipsum dolor sit amet, consectetuer</b>Etiam rhoncus. Maecenas tempus, tellus eget condimentum rhoncus, sem ... <a class="more" href="#">more »</a></article>
  <a class="more" href="#" style="margin-left:-1px">All News »</a>
</section>

<section class="col" style="left:394px">
  <h2>Harlow's Features</h2>
  <ul class="features">
    <li>Documented Quality Assurance Laboratory</li>
    <li>Accurate &amp; reliable service from long-standing Employees</li>
    <li>Mechanical Engineer on Staff with Manufacturing Experience (Kestrel Systems)</li>
    <li class="plain">Customized Packaging/Labeling</li>
    <li>Free Delivery for VMI Customers (Ridgeport/North Valley)</li>
    <li>VMI Emergency After-Hours Service (24/7)</li>
    <li>Complete Lot Traceability</li>
    <li>Point of Use reporting: Trends, efficiencies, opportunities</li>
  </ul>
  <a class="more" href="#">Learn More »</a>
</section>

<section class="col lean" style="left:617px">
  <h2>Lean Resources</h2>
  <h3>Northridge Lean Management Consortium</h3>
  <ul><li>SPE Denver 2013: Lean Summit</li><li>Advanced Visual Management</li></ul>
  <h3>Society for Production Excellence (SPE)</h3>
  <ul><li>SPE Denver 2013: Lean Summit</li><li>Advanced Visual Management</li><li>Mastering Lean Product Development Webinar</li></ul>
  <a class="more" href="#">Learn More »</a>
</section>

<section class="partners">
  <h2>Our Partners</h2>
  <svg width="20" height="42" viewBox="0 0 20 42"><path d="M2 2l15 19L2 40" fill="none" stroke="#ddd" stroke-width="3"/></svg>
  <div class="badge" style="left:157px;width:130px"><span style="width:108px;height:30px"></span></div>
  <div class="badge" style="left:300px;width:106px"><span style="width:54px;height:26px;border-radius:3px"></span></div>
  <div class="badge" style="left:417px;width:106px"><span style="width:56px;height:38px;border-radius:0;background:#e8621c"></span></div>
  <div class="badge" style="left:536px;width:106px"><span style="width:86px;height:28px"></span></div>
</section>

<footer class="site-footer">
  <div class="f-menu">
    <h2>Menu</h2>
    <ul style="left:0"><li>Home</li><li>About Us</li><li>Products</li><li>Features</li></ul>
    <ul style="left:87px"><li>News</li><li>Resources</li><li>Careers</li><li>Contact Us</li></ul>
  </div>
  <div class="f-sep" style="left:337px"></div>
  <div class="f-contact">
    <h2>Contact Info</h2>
    <address>2207 Foundry Lane<br>Ridgeport, NV 89000<br>PO Box 7710</address>
    <dl>
      <dt>Service:</dt><dd>+1 555 019 4410</dd>
      <dt>Toll Free USA:</dt><dd>+1 555 014 2291</dd>
      <dt>Fax:</dt><dd>+1 555 019 4477</dd>
      <dt>Email:</dt><dd><u>info@harlowrivet-sample.com</u></dd>
    </dl>
  </div>
  <div class="f-sep" style="left:657px"></div>
  <div class="f-social">
    <h2>We Are Social</h2>
    <ul><li><i></i>Became a Fan</li><li><i></i>Follow Us</li><li><i></i>Join Us</li></ul>
  </div>
</footer>

<div class="legal">Terms and Conditions &nbsp;|&nbsp; Privacy Policy<br>© Copyright 2012. All Rights Reserved. Harlow Rivet &amp; Pin Inc.</div>
</body>
</html>
```